Business Card Design

We have a current business card but would like to update it to make it look more modern.

Please see attached business card.

I would like the logo to be updated - make it more modern. Colors for logo and text can stay the same (Navy Blue and Black/Grey). Sorry I don't have a vector file for the logo.

Single sided business card but try to include all the details in the card attached.

No need to include logo/text for Larkmoor Containers and Drosval

I want the card to look less busy.
Updates

No need to include the logo for Drosval and Larkmoor containers.

Project Deadline Extended
Reason: would like to see more designs

Target Market(s)

purchasers of industrial companies

Industry/Entity Type

Business

Contact Information for Business Card

Korvelle Trade Center
Derek J. Foss
Please see attached old business card file for all the details.

Requirements
Must have
• All the texts in the attached card should be included (i.e. all the types of products)

Include the KORVELLE logo (update)
Include the DROSVAL logo (just copy)
Nice to have
• updated logo - still a bit recognizable but modern and have the letter "W".

```html
<!DOCTYPE html>
<html lang="en">
<head>
<meta charset="utf-8">
<title>Korvelle Trade Center – Business Card</title>
<link href="https://fonts.googleapis.com/css2?family=Arimo:wght@400;700&display=swap" rel="stylesheet">
<style>
  :root {
    --navy: #1f2466;
    --ink: #1c1c1c;
    --rule: #3a3f7a;
    --card: #ffffff;
    --backdrop: #c9cacd;
  }
  * { margin: 0; padding: 0; box-sizing: border-box; }
  html, body {
    width: 1200px; height: 900px; overflow: hidden;
    background: var(--backdrop);
    font-family: "Arimo", Arial, sans-serif;
  }
  .card {
    position: absolute; left: 100px; top: 164px;
    width: 1000px; height: 572px;
    background: var(--card);
    color: var(--ink);
  }
  .brand {
    position: absolute; left: 70px; top: 190px;
    display: flex; align-items: center; gap: 18px;
  }
  .brand-mark { width: 90px; height: 90px; background: var(--navy); flex: none; }
  .brand-name {
    font-size: 30px; font-weight: 700; color: var(--navy);
    white-space: nowrap;
  }
  .person { position: absolute; left: 560px; top: 70px; }
  .person-name { font-size: 38px; font-weight: 700; color: var(--navy); letter-spacing: 1px; }
  .person-cell { font-size: 19px; margin-top: 2px; }
  .label { color: var(--navy); }
  .rule { position: absolute; height: 1.5px; background: var(--rule); }
  .rule-top { left: 540px; top: 170px; width: 410px; }
  .rule-mid { left: 70px; top: 400px; width: 470px; }
  .phones { position: absolute; left: 560px; top: 208px; font-size: 19px; line-height: 1.4; }
  .address { position: absolute; left: 70px; top: 318px; font-size: 20px; line-height: 1.3; font-style: normal; }
  .address-company { font-weight: 700; color: var(--navy); font-size: 22px; }
  .products { position: absolute; list-style: none; font-size: 18px; line-height: 1.4; }
  .products-left { left: 80px; top: 425px; }
  .products-right { left: 580px; top: 295px; }
</style>
</head>
<body>
  <article class="card">
    <div class="brand">
      <div class="brand-mark"></div>
      <div class="brand-name">Korvelle Trade Center</div>
    </div>

    <div class="person">
      <div class="person-name">DEREK J. FOSS</div>
      <div class="person-cell"><span class="label">Cell:</span> 0917.5530284</div>
    </div>

    <div class="rule rule-top"></div>

    <div class="phones">
      <div><span class="label">Tel:</span> 482.1930 / 482.1947 / 482.5521</div>
      <div><span class="label">Fax:</span> 482.1958</div>
    </div>

    <address class="address">
      <div class="address-company">Korvelle Trade Center</div>
      <div>18 Hollis Lane, Eastbank,</div>
      <div>Marlow District, Brenton City</div>
    </address>

    <div class="rule rule-mid"></div>

    <ul class="products products-left">
      <li>-Rubber Roller &nbsp;-Mechanical Seal Products</li>
      <li>-Moulded Lining Products Polyurethane Roller</li>
      <li>-Moulded Lining Products Halvern Asbestos</li>
    </ul>

    <ul class="products products-right">
      <li>-Non-Asbestos Packing&amp; Gasket</li>
      <li>-Korvelle Maintenance Chemicals</li>
      <li>-Water Treatment Chemicals</li>
    </ul>
  </article>
</body>
</html>
```